Web re-design project www.vempresoft.com

We need a corporate website for a startup company called Vempre Labs. The company offers web-based worksite management system for big construction companies. In short, replacing annoying papers with iPads.
We need the site main page to provide basic overview of the company and then inner page layout for displaying news and detailed information about products.
Currently we have a site up at:
http://www.vempresoft.com/en/main
but as you can see the graphic design is a bit lacking in quality(implemented by a tech guy :)
We need you to pimp that web site design up!
There is possibility for more freelance work in the future related to our web products, slide show designs and printed marketing materials.
Our main product is LOMVI. You can find a short presentation about what it does here:
http://www.vempresoft.com/en/lomvi
Here you can find packages of images and screenshots related to our company:
https://files.plimbox.net/u/7719026/vempre_images.zip
https://files.plimbox.net/u/7719026/vempresoft%20images2.zip
Product logo svg can be found here:
https://files.plimbox.net/u/7719026/LOMVI-logo.svg
Your are not forced to use those images, but hopefully there will be something that is useful.
Hope to hear from you guys soon!
Cheers,
Ossi
Update:
We will be using LOMVI logo as the company brand. I don't like our current Vempre Labs company logo, so that doesn't need to be included in the site design.
Update 2:
I like website designs that are "light", elegant and pretty simplistic. One example is our product login page (screenshot included in files).
Update 3:
Sites from the same industry / type of products:
http://www.rakmoda.fi/
http://www.quarvelgrid.com/products/software/network-applications/fieldsync-3d
http://www.dornvex.com/construction/heavy-civil/software-solutions/Linked-Network.aspx?dtID=overview&
Target audience for the website is companies in the construction sector, and possibly corporate investors
Graphic Design

```html
<!DOCTYPE html>
<html lang="en">
<head>
<meta charset="utf-8">
<title>LOMVI – Vempre Labs</title>
<link rel="stylesheet" href="https://fonts.googleapis.com/css2?family=Source+Sans+3:ital,wght@0,400;0,600;0,700;1,400;1,600&family=Poppins:wght@600&display=swap">
<style>
:root{
  --red:#d91f26;
  --red-dark:#b5151b;
  --ink:#2b2b2b;
  --text:#555;
  --muted:#777;
  --top-bg:#f2f2f2;
  --texture:#e8e6e2;
  --nav:#2a2a2a;
  --nav-top:#3b3b3b;
  --rule:#cfcfcf;
  --footer:#e9e9e9;
}
*{box-sizing:border-box;margin:0;padding:0}
html,body{width:1200px;height:1038px;overflow:hidden}
body{
  position:relative;
  font-family:"Source Sans 3",sans-serif;
  color:var(--text);
  background:linear-gradient(#f4f4f4 0,#f0f0f0 127px,var(--texture) 129px,var(--texture) 503px,#f9f9f9 560px,#fff 600px,#fff 940px,var(--footer) 940px);
}
.abs{position:absolute}
a{color:inherit;text-decoration:none}

/* header */
.brand{left:205px;top:27px;display:flex;align-items:center;gap:30px}
.brand-dot{width:22px;height:22px;border-radius:50%;background:var(--red)}
.brand-name{font-size:62px;font-weight:400;color:#111;letter-spacing:1px;line-height:1}
.util{right:115px;top:8px;font-size:12.5px;color:var(--ink);display:flex;gap:7px}
.util .sep{color:#999}
.util .on{color:var(--red)}
.search{left:834px;top:47px;width:224px;height:25px;background:#fff;border:1px solid #b9b9b9;box-shadow:0 1px 2px rgba(0,0,0,.15);font-size:12px;font-style:italic;color:#888;padding:4px 9px}
.search svg{position:absolute;right:5px;top:2px}

/* nav */
.nav{left:141px;top:115px;width:918px;height:42px;border-radius:4px 4px 0 0;background:linear-gradient(var(--nav-top),var(--nav))}
.nav a{position:absolute;top:0;height:42px;line-height:44px;color:#fff;font-size:14.5px;transform:translateX(-50%);white-space:nowrap}
.nav .home{left:0;transform:none;width:117px;text-align:center;background:linear-gradient(#e8262d,var(--red-dark));border-radius:4px 0 0 0}
.nav .div{position:absolute;top:8px;width:1px;height:28px;background:#151515;box-shadow:1px 0 0 #4a4a4a}

/* slider */
.slider{left:141px;top:166px;width:919px;height:378px;border:2px solid #fff;border-radius:4px;box-shadow:0 10px 12px -6px rgba(0,0,0,.3);
  background:radial-gradient(ellipse at 20% 60%,#d7dc3c 0,#c6c842 22%,transparent 45%),radial-gradient(ellipse at 30% 75%,#d23a30 0,transparent 22%),linear-gradient(100deg,#8a7d56 0,#b9b27c 35%,#9fa66a 55%,#7c8a57 80%,#5f6a44 100%)}
.caption{left:523px;top:274px;width:545px;height:161px;background:rgba(25,25,25,.72);padding:13px 18px 0 0;text-align:right;font-family:"Poppins",sans-serif;font-weight:600;font-size:29px;letter-spacing:-.2px;line-height:45px;white-space:nowrap;color:#fff;text-shadow:0 2px 3px rgba(0,0,0,.5)}
.fold{left:1060px;top:435px}
.dots{left:549px;top:508px;display:flex;gap:6px}
.dots span{width:21px;height:21px;border-radius:50%;background:#3a3a3a;opacity:.85}
.dots span:first-child{background:var(--red);opacity:1}

/* columns */
.col h2{font-size:22.5px;font-weight:400;color:var(--ink);line-height:1}
.col p{font-size:12.8px;line-height:22.4px}
.col-rule{top:595px;width:1px;height:193px;background:var(--rule)}
.thumb{width:280px;height:105px;border-radius:7px}
.site-photo{background:linear-gradient(90deg,#7a5a3e,#b8b04a 40%,#c9d04b 60%,#6c6a58)}
.product-box{width:288px;height:108px;border:1px solid #d6d6d6;border-radius:7px;background:linear-gradient(#fff,#e7e7e7);box-shadow:inset 0 0 0 3px #fff;display:flex;align-items:center;justify-content:center;gap:16px}
.product-box .brand-dot{width:14px;height:14px}
.product-box span{font-size:44px;color:#111;letter-spacing:1px}
.btn{height:25px;line-height:25px;border-radius:3px;background:linear-gradient(#e3262d,var(--red-dark));color:#fff;font-weight:600;font-size:14px;text-align:center}

.news-item{left:774px;width:258px;height:78px}
.date{position:absolute;left:2px;top:0;width:50px;height:50px;border-radius:50%;background:var(--red);color:#fff;text-align:center;font-style:italic;box-shadow:0 0 0 2px #fff,0 0 0 3px #e3b3b5}
.date b{display:block;font-size:24px;font-weight:600;line-height:24px;margin-top:5px}
.date i{display:block;font-size:13px;line-height:13px}
.news-item p{position:absolute;left:67px;top:-10px;width:195px;font-size:12.5px;line-height:19.5px}
.news-item p em{color:var(--red)}
.news-rule{left:776px;width:256px;height:1px;background:var(--rule)}

/* footer */
.foot-links{left:142px;top:967px;font-size:12.5px;color:var(--ink)}
.foot-links .sep{color:#888;margin:0 4px}
.copy{left:145px;top:995px;font-size:11.5px;color:var(--red)}
.copy strong{color:var(--ink);font-weight:400}
.follow{left:916px;top:963px;font-size:14px;font-weight:600;color:#555}
.social{left:916px;top:996px;display:flex;gap:9px}
.social span{width:16px;height:16px;border-radius:2px;background:#7b8794}
</style>
</head>
<body>

<header>
  <div class="abs brand"><span class="brand-dot"></span><span class="brand-name">LOMVI</span></div>
  <nav class="abs util">
    <a href="#">Login</a><span class="sep">|</span>
    <a href="#">Register</a><span class="sep">|</span>
    <a href="#">FAQ's</a><span class="sep">|</span>
    <a href="#">Site Map</a><span class="sep">|</span>
    <a href="#" class="on">EN</a><span class="sep" style="color:var(--red)">|</span>
    <a href="#">FI</a>
  </nav>
  <div class="abs search">Search keyworks...
    <svg width="24" height="20" viewBox="0 0 24 20"><circle cx="9" cy="8" r="6" fill="none" stroke="#d91f26" stroke-width="2.5"/><line x1="13.5" y1="12" x2="21" y2="18" stroke="#d91f26" stroke-width="3.5" stroke-linecap="round"/></svg>
  </div>
  <nav class="abs nav">
    <a href="#" class="home">Home</a>
    <a href="#" style="left:199px">About Us</a>
    <span class="div" style="left:277px"></span>
    <a href="#" style="left:353px">Products</a>
    <span class="div" style="left:431px"></span>
    <a href="#" style="left:507px">News</a>
    <span class="div" style="left:573px"></span>
    <a href="#" style="left:657px">Contact Us</a>
  </nav>
</header>

<section>
  <div class="abs slider" role="img" aria-label="Smiling road worker in a hard hat and safety vest holding a tablet on a construction site"></div>
  <div class="abs caption">Lomvi is a cloud-based service<br>for road construction projects<br>and it's going full steam!</div>
  <svg class="abs fold" width="9" height="10" viewBox="0 0 9 10"><polygon points="0,0 9,0 0,10" fill="#333"/></svg>
  <div class="abs dots"><span></span><span></span><span></span><span></span></div>
</section>

<main>
  <div class="abs col" style="left:141px;top:593px;width:285px">
    <h2>Welcome to our site</h2>
    <div class="thumb site-photo" role="img" aria-label="Construction crew in safety vests and helmets beside an excavator" style="margin-top:11px"></div>
    <p style="margin-top:10px">Aliquam molestie, mi et imperdiet euismod, dui purus auctor tellus, et interdum lacus lectus et ante. Sed accumsan sollicitudin sapien, sit amet adipiscing turpis gravida ac. In congue, neque ac lobortis volutpat, libero mauris varius mi, vitae suscipit ipsum ligula vitae risus.</p>
  </div>
  <a href="#" class="abs btn" style="left:358px;top:891px;width:59px">More</a>
  <div class="abs col-rule" style="left:445px"></div>

  <div class="abs col" style="left:460px;top:593px;width:290px">
    <h2>Our Products</h2>
    <div class="product-box" style="margin-top:11px"><span class="brand-dot"></span><span>LOMVI</span></div>
    <p style="margin-top:7px;width:285px">Aliquam molestie, mi et imperdiet euismod, dui purus auctor tellus, et interdum lacus lectus et ante. Sed accumsan sollicitudin sapien, sit amet adipiscing turpis gravida ac. In congue, neque ac lobortis volutpat, libero mauris varius mi, vitae suscipit ipsum ligula vitae risus.</p>
  </div>
  <a href="#" class="abs btn" style="left:677px;top:891px;width:59px">More</a>
  <div class="abs col-rule" style="left:756px"></div>

  <div class="abs col" style="left:774px;top:593px"><h2>Update News</h2></div>
  <article class="abs news-item" style="top:629px">
    <div class="date"><b>25</b><i>Oct</i></div>
    <p>Aliquam molestie, mi et imperdiet euismod, dui purus auctor tellus, et interdum lacus.. <em>Read More</em></p>
  </article>
  <div class="abs news-rule" style="top:692px"></div>
  <article class="abs news-item" style="top:704px">
    <div class="date"><b>20</b><i>Oct</i></div>
    <p>Aliquam molestie, mi et imperdiet euismod, dui purus auctor tellus, et interdum lacus.. <em>Read More</em></p>
  </article>
  <div class="abs news-rule" style="top:770px"></div>
  <article class="abs news-item" style="top:782px">
    <div class="date"><b>18</b><i>Oct</i></div>
    <p>Aliquam molestie, mi et imperdiet euismod, dui purus auctor tellus, et interdum lacus.. <em>Read More</em></p>
  </article>
  <a href="#" class="abs btn" style="left:953px;top:891px;width:78px">Read All</a>
</main>

<footer>
  <nav class="abs foot-links">
    <a href="#">Home</a><span class="sep">/</span><a href="#">About Us</a><span class="sep">/</span><a href="#">Products</a><span class="sep">/</span><a href="#">News</a><span class="sep">/</span><a href="#">Contact Us</a>
  </nav>
  <div class="abs copy">© 2012 <strong>vempresoft.com</strong>. All Right Reserved</div>
  <div class="abs follow">Follow us on:</div>
  <div class="abs social" aria-label="Social links">
    <span></span><span></span><span></span><span></span><span></span><span></span>
  </div>
</footer>

</body>
</html>
```